Online-Marketing Material für einen Online Kurs
Zielgruppe
Online Kurs SerienTitel 'Vom Nebel zum Gipfel' Untertitel: 'Mache aus Deinem schwersten Tag einen Anfang Deiner Stärke!' Zielgruppe: Menschen mit chronischen Rückenschmerzen
Titel: Chronische Rückenschmerzen
Aufgabenstellung
1. Kleine Änderung des Logos: Steady MIndframe raus und Dr. Lukas Brennwald in leuchtendem grün rein
Es gibt zwei Titel: Serientitel und den Kurstitel
2. Logo und Bild für Online Kurs für kursolo und andere Nutzungen, Akzentfarbe soll grün sein. Das Vitabrook Logo kann klein sein, der Titel ist am wichtigsten.
3. Ein Bild sollte für kursolo quadratisch sein.
4. Vielleicht eine Foto Collage von Mensch mit Schmerzen und Mensch mit Power

```html
<!DOCTYPE html>
<html lang="de">
<head>
<meta charset="utf-8">
<title>Vom Nebel zum Gipfel – Formate</title>
<link rel="stylesheet" href="https://fonts.googleapis.com/css2?family=Bebas+Neue&family=Montserrat:wght@400;600;700&display=swap">
<style>
  :root {
    --board: #e4e4e4;
    --panel-dark: #262626;
    --white: #ffffff;
    --green: #18e02a;
    --green-deep: #14532a;
    --label: #333333;
    --sky-warm: #e39a5c;
    --sky-glow: #f2b877;
    --shadow-figure: #3b3330;
  }
  * { margin: 0; padding: 0; box-sizing: border-box; }
  html, body { width: 1200px; height: 879px; overflow: hidden; }
  body { background: var(--board); font-family: "Montserrat", sans-serif; position: relative; }

  .format { position: absolute; top: 152px; width: 332px; background: var(--panel-dark); overflow: hidden; }
  .format--square { left: 78px; height: 332px; }
  .format--portrait { left: 427px; height: 414px; }
  .format--story { left: 775px; height: 590px; }

  .hero-photo {
    position: absolute; left: 0; top: 0; width: 100%;
    background:
      linear-gradient(180deg, rgba(38,38,38,0) 55%, var(--panel-dark) 100%),
      linear-gradient(100deg, var(--shadow-figure) 0%, #6e5242 30%, var(--sky-warm) 62%, var(--sky-glow) 75%, #b9764a 100%);
  }
  .format--square .hero-photo { height: 230px; }
  .format--portrait .hero-photo { height: 301px; }
  .format--story .hero-photo { height: 348px; }

  .series-title {
    position: absolute; left: 29px;
    font-family: "Bebas Neue", sans-serif; font-size: 44px; line-height: 41px;
    color: var(--white); letter-spacing: 0.5px;
  }
  .series-title .line { display: block; }
  .series-title .line--accent { display: flex; align-items: center; gap: 8px; color: var(--green); padding-left: 4px; }
  .chevrons { width: 85px; height: 28px; flex: none; margin-top: -6px; }
  .format--square .series-title { top: 116px; }
  .format--portrait .series-title { top: 165px; font-size: 46px; line-height: 44px; }
  .format--story .series-title { top: 302px; font-size: 48px; line-height: 45px; }

  .series-subtitle {
    position: absolute; left: 28px; width: 290px;
    font-size: 12.5px; line-height: 17.5px; color: var(--white); font-weight: 400; letter-spacing: 0.3px;
  }
  .series-subtitle strong { font-weight: 700; }
  .format--square .series-subtitle { top: 246px; }
  .format--portrait .series-subtitle { top: 308px; font-size: 13px; line-height: 19.5px; }
  .format--story .series-subtitle { top: 444px; font-size: 15px; line-height: 23px; width: 300px; }

  .brand-mark { position: absolute; right: 24px; text-align: right; }
  .brand-name { font-size: 11px; font-weight: 600; color: var(--white); letter-spacing: 0.5px; line-height: 12px; }
  .brand-host { font-size: 6.5px; font-weight: 600; color: var(--green); line-height: 9px; }
  .format--square .brand-mark { top: 294px; }
  .format--portrait .brand-mark { top: 366px; }
  .format--story .brand-mark { top: 520px; right: 28px; }

  .format-label {
    position: absolute; width: 260px; text-align: center;
    font-size: 21px; font-weight: 700; color: var(--label);
  }
  .format-label--square { left: 114px; top: 540px; }
  .format-label--portrait { left: 462px; top: 628px; }
  .format-label--story { left: 811px; top: 793px; }
</style>
</head>
<body>

<svg width="0" height="0" style="position:absolute">
  <defs>
    <linearGradient id="chevron-fade" x1="0" x2="1" y1="0" y2="0">
      <stop offset="0" stop-color="#14532a"/>
      <stop offset="1" stop-color="#18e02a"/>
    </linearGradient>
    <symbol id="chevron-row" viewBox="0 0 85 28">
      <path d="M0 0h12l12 14-12 14H0l12-14z" fill="#1d4a27"/>
      <path d="M20 0h12l12 14-12 14H20l12-14z" fill="#1c7a2c"/>
      <path d="M40 0h12l12 14-12 14H40l12-14z" fill="#16a82a"/>
      <path d="M60 0h12l13 14-13 14H60l12-14z" fill="#18e02a"/>
    </symbol>
  </defs>
</svg>

<section class="format format--square">
  <div class="hero-photo" role="img" aria-label="Fotocollage: Frau mit Kopf in der Hand im Schatten links, Frau mit erhobener Faust vor orangem Sonnenuntergangshimmel rechts"></div>
  <h2 class="series-title">
    <span class="line">Vom</span>
    <span class="line">Nebel</span>
    <span class="line line--accent"><svg class="chevrons"><use href="#chevron-row"/></svg>Zum Gipfel</span>
  </h2>
  <p class="series-subtitle">MACHE AUS DEINEM SCHWERSTEN TAG <strong>EINEN ANFANG DEINER STÄRKE!</strong></p>
  <div class="brand-mark">
    <div class="brand-name">VITABROOK</div>
    <div class="brand-host">Dr. Lukas Brennwald</div>
  </div>
</section>

<section class="format format--portrait">
  <div class="hero-photo" role="img" aria-label="Fotocollage: Frau mit Kopf in der Hand im Schatten links, Frau mit erhobener Faust vor orangem Sonnenuntergangshimmel rechts"></div>
  <h2 class="series-title">
    <span class="line">Vom</span>
    <span class="line">Nebel</span>
    <span class="line line--accent"><svg class="chevrons"><use href="#chevron-row"/></svg>Zum Gipfel</span>
  </h2>
  <p class="series-subtitle">MACHE AUS DEINEM SCHWERSTEN TAG <strong>EINEN ANFANG DEINER STÄRKE!</strong></p>
  <div class="brand-mark">
    <div class="brand-name">VITABROOK</div>
    <div class="brand-host">Dr. Lukas Brennwald</div>
  </div>
</section>

<section class="format format--story">
  <div class="hero-photo" role="img" aria-label="Fotocollage: Frau mit Kopf in der Hand im Schatten links, Frau mit erhobener Faust vor orangem Sonnenuntergangshimmel rechts"></div>
  <h2 class="series-title">
    <span class="line">Vom</span>
    <span class="line">Nebel</span>
    <span class="line line--accent"><svg class="chevrons"><use href="#chevron-row"/></svg>Zum Gipfel</span>
  </h2>
  <p class="series-subtitle">MACHE AUS DEINEM SCHWERSTEN TAG <strong>EINEN ANFANG DEINER STÄRKE!</strong></p>
  <div class="brand-mark">
    <div class="brand-name">VITABROOK</div>
    <div class="brand-host">Dr. Lukas Brennwald</div>
  </div>
</section>

<p class="format-label format-label--square">1080px x 1080px</p>
<p class="format-label format-label--portrait">1080px x 1350px</p>
<p class="format-label format-label--story">1080px x 1920px</p>

</body>
</html>
```